Business card for Sports Apparel business

DOUBLE SIDED DESIGN
We need business cards for a new sports apparel business. We are developing a protective headband for soccer initially.
Corvell is focused on designing and developing head protection products to reduce the likelihood of concussion when playing sports. Exploring and understanding medical insights, material science research, current and former players experiences and governing bodies guidelines has allowed Corvell to develop the safety, style, form and function requirements of a suitable product to bring to market.
Target Market(s)
Mums buying kits for the sons and daughters. Amateur footballers.
Industry/Entity Type
Sporting Good
Contact Information for Business Card
Martin Ashgrove - CEO
Mobile: +44 7391608254
Email: martin@corvell.co.uk
Tel: 0208 5143927
Helena Pardoe - COO
Mob: +44 7356 409183
Email: helena@corvell.co.uk
Tel: 0208 5143927
Duncan Wyvern - CCO
Mob: +44 7468 230517
Email: duncan@corvell.co.uk
Tel: 0208 5143927
Look and feel

```html
<!DOCTYPE html>
<html lang="en">
<head>
<meta charset="utf-8">
<title>Corvell business card</title>
<link rel="stylesheet" href="https://fonts.googleapis.com/css2?family=Open+Sans:wght@400;600;700&display=swap">
<style>
  :root {
    --stage: #3d3c3b;
    --brand-blue: #145a90;
    --brand-blue-dark: #0f4c7d;
    --slate: #555657;
    --ink: #4a4a4a;
    --paper: #f4f4f5;
    --paper-edge: #e2e2e4;
    --white: #ffffff;
  }
  * { box-sizing: border-box; margin: 0; padding: 0; }
  html, body {
    width: 1200px; height: 960px; overflow: hidden;
    background: var(--stage);
    font-family: "Open Sans", Arial, sans-serif;
  }
  .sheet {
    width: 1200px; height: 960px;
    display: flex; flex-direction: column; align-items: center; justify-content: center;
    gap: 36px;
  }
  .card {
    position: relative;
    width: 660px; height: 420px;
    overflow: hidden;
    box-shadow: 0 10px 30px rgba(0,0,0,.35);
  }

  /* Back side */
  .card--back {
    background: linear-gradient(160deg, var(--brand-blue) 0%, var(--brand-blue-dark) 100%);
    display: flex; align-items: center; justify-content: center;
  }
  .wordmark {
    display: flex; align-items: center; gap: 18px;
    font-weight: 700; text-transform: uppercase; letter-spacing: 2px; line-height: 1;
  }
  .wordmark__mark { display: block; }
  .card--back .wordmark { color: var(--white); font-size: 70px; }
  .card--back .wordmark__mark { width: 40px; height: 40px; background: var(--white); }

  /* Front side */
  .card--front {
    background: radial-gradient(ellipse at 58% 40%, var(--white) 0%, var(--paper) 45%, var(--paper-edge) 100%);
  }
  .card--front .wordmark {
    position: absolute; left: 56px; top: 84px;
    color: var(--ink); font-size: 78px;
  }
  .card--front .wordmark__mark { width: 44px; height: 44px; background: var(--brand-blue); }
  .name-band {
    position: absolute; left: 0; top: 186px;
    width: 560px; height: 52px;
    background: var(--brand-blue);
    display: flex; align-items: center; padding-left: 46px;
  }
  .name-band__name { color: var(--white); font-size: 26px; font-weight: 600; }
  .accent-block {
    position: absolute; left: 572px; top: 186px;
    width: 88px; height: 52px; background: var(--slate);
  }
  .role {
    position: absolute; left: 62px; top: 252px;
    color: var(--ink); font-size: 20px; font-weight: 600; letter-spacing: 6px;
  }
  .contact {
    position: absolute; display: flex; align-items: center; gap: 14px;
    color: var(--ink); font-size: 20px; font-weight: 600;
  }
  .contact svg { width: 26px; height: 26px; flex: none; }
  .contact--mobile { left: 74px; top: 308px; }
  .contact--email { left: 74px; top: 354px; }
  .contact--tel { left: 370px; top: 252px; }
</style>
</head>
<body>
<main class="sheet">
  <section class="card card--back" aria-label="Card back">
    <div class="wordmark"><span class="wordmark__mark"></span><span>Corvell</span></div>
  </section>

  <section class="card card--front" aria-label="Card front">
    <div class="wordmark"><span class="wordmark__mark"></span><span>Corvell</span></div>
    <div class="name-band"><span class="name-band__name">Martin Ashgrove</span></div>
    <div class="accent-block"></div>
    <p class="role">CEO</p>

    <p class="contact contact--tel">
      <svg viewBox="0 0 24 24" fill="none" stroke="#145a90" stroke-width="1.6" stroke-linejoin="round" aria-hidden="true">
        <path d="M5 3h4l2 5-2.5 1.5a11 11 0 0 0 6 6L16 13l5 2v4a2 2 0 0 1-2 2A17 17 0 0 1 3 5a2 2 0 0 1 2-2z"/>
      </svg>
      <span>0208 5143927</span>
    </p>
    <p class="contact contact--mobile">
      <svg viewBox="0 0 24 24" fill="none" stroke="#145a90" stroke-width="1.6" aria-hidden="true">
        <rect x="6" y="2" width="12" height="20" rx="2"/><line x1="11" y1="18.5" x2="13" y2="18.5"/>
      </svg>
      <span>+44 7391608254</span>
    </p>
    <p class="contact contact--email">
      <svg viewBox="0 0 24 24" fill="none" stroke="#145a90" stroke-width="1.6" stroke-linejoin="round" aria-hidden="true">
        <rect x="2" y="5" width="20" height="14"/><path d="M2 5l10 8 10-8M2 19l7-7M22 19l-7-7"/>
      </svg>
      <span>martin@corvell.co.uk</span>
    </p>
  </section>
</main>
</body>
</html>
```